Redesign of existing business card

I would like the "signage" attachment converted into a business card. This needs to be double sided aswell, keeping the phone number and names on the front, and the email + website on the back.

Second attachment is the current business card design.

Larger font for contact details is required.

Must keep to original color themes (electric blue, silver/grey etc)

Back of the card to have blue background with white writing.

Industry/Entity Type

Business

Contact Information for Business Card

Refer to existing design from attachments

Requirements
Must have
• Refer to existing design from attachments
Nice to have

```html
<!DOCTYPE html>
<html lang="en">
<head>
<meta charset="utf-8">
<title>Voltara Electro Services – Business Card</title>
<link rel="stylesheet" href="https://fonts.googleapis.com/css2?family=Open+Sans:wght@400;600;700;800&display=swap">
<style>
  :root {
    --electric-blue: #1a1af5;
    --silver: #a9a9ab;
    --silver-dark: #858588;
    --silver-light: #d2d2d4;
    --ink: #4a4a4d;
    --card: #ffffff;
    --front-card: #f7f7f7;
    --backdrop: #e6e6e8;
  }
  * { box-sizing: border-box; margin: 0; padding: 0; }
  html, body {
    width: 1200px; height: 900px; overflow: hidden;
    background: var(--backdrop);
    font-family: "Open Sans", Arial, sans-serif;
    color: var(--ink);
  }
  .canvas { position: relative; width: 1200px; height: 900px; }

  .card {
    position: absolute;
    border-radius: 14px;
    overflow: hidden;
    box-shadow: 0 6px 18px rgba(0,0,0,0.12);
  }

  /* Front */
  .card-front {
    left: 310px; top: 55px; width: 558px; height: 343px;
    background: var(--front-card);
  }
  .brand-name {
    color: var(--electric-blue);
    font-weight: 800;
    letter-spacing: 1px;
    line-height: 1;
  }
  .card-front .brand-name { position: absolute; left: 40px; top: 40px; }
  .brand-name .brand-main { display: block; font-size: 54px; }
  .brand-name .brand-sub { display: block; font-size: 21px; letter-spacing: 1.5px; margin-top: 4px; }
  .licence { position: absolute; left: 40px; top: 131px; font-size: 14px; }
  .person-name {
    position: absolute; left: 40px; top: 168px;
    font-size: 22px; font-weight: 600; color: var(--electric-blue);
  }
  .person-role { position: absolute; left: 40px; top: 196px; font-size: 16px; }
  .contact-list { position: absolute; left: 40px; top: 232px; list-style: none; }
  .contact-list li {
    display: flex; align-items: center; gap: 10px;
    font-size: 18.5px; height: 25px;
  }
  .icon { width: 16px; height: 16px; fill: var(--electric-blue); flex: none; }
  .side-panel {
    position: absolute; right: 0; top: 0; width: 205px; height: 343px;
    background: linear-gradient(160deg, var(--silver-light), var(--silver) 55%, var(--silver-dark));
    clip-path: polygon(35% 0, 100% 0, 100% 100%, 0 100%);
  }

  /* Back */
  .card-back {
    left: 400px; top: 505px; width: 555px; height: 345px;
    background: var(--card);
  }
  .card-back .brand-name {
    position: absolute; left: 0; right: 0; top: 36px;
    display: flex; align-items: center; justify-content: center; gap: 14px;
  }
  .brand-dot {
    width: 58px; height: 58px; border-radius: 50%;
    background: var(--electric-blue);
  }
  .card-back .brand-main { font-size: 50px; }
  .card-back .brand-sub { font-size: 19px; }
  .tagline {
    position: absolute; left: 0; right: 0; top: 143px;
    text-align: center; font-size: 18px; font-weight: 600; color: var(--ink);
  }
  .tagline strong { color: var(--electric-blue); font-weight: 600; }
  .services {
    position: absolute; top: 190px; list-style: none;
    font-size: 15px; line-height: 20px;
  }
  .services-left { left: 84px; }
  .services-right { right: 88px; text-align: right; }
  .services-left li::before { content: "• "; color: var(--electric-blue); }
  .services-right li::after { content: " •"; color: var(--electric-blue); }
  .quote-band {
    position: absolute; left: 0; right: 0; bottom: 0; height: 82px;
    background: var(--electric-blue); color: #fff;
    display: flex; flex-direction: column; align-items: center; justify-content: center;
    gap: 3px; font-size: 15px;
  }
  .quote-contacts { display: flex; gap: 16px; font-size: 16.5px; }
  .quote-contacts span { display: flex; align-items: center; gap: 6px; }
  .quote-band .icon { fill: #fff; width: 15px; height: 15px; }
</style>
</head>
<body>
<div class="canvas">
  <svg width="0" height="0" style="position:absolute">
    <defs>
      <symbol id="icon-phone" viewBox="0 0 16 16"><path d="M1 5c0-2 3-3 7-3s7 1 7 3v1h-3V4.5H4V6H1zM4 7h8l3 4v3H1v-3zm4 1.5a2 2 0 1 0 0 4 2 2 0 0 0 0-4z"/></symbol>
      <symbol id="icon-mail" viewBox="0 0 16 16"><path d="M1 3h14v10H1zm1.5 1.5v.3L8 9l5.5-4.2v-.3zm0 2.2v4.8h11V6.7L8 11z"/></symbol>
      <symbol id="icon-globe" viewBox="0 0 16 16"><path d="M8 1a7 7 0 1 0 0 14A7 7 0 0 0 8 1zm-1 2.5 1.5 1-1 1.5 1.5 1.5-.5 2L6 8 4 7l.5-2zm3.5 5 2 .5-1 3-2 .5z"/></symbol>
    </defs>
  </svg>

  <section class="card card-front">
    <div class="brand-name"><span class="brand-main">VOLTARA</span><span class="brand-sub">ELECTRO SERVICES</span></div>
    <p class="licence">EC 20491</p>
    <h1 class="person-name">DANIEL KOVAC</h1>
    <p class="person-role">DIRECTOR</p>
    <ul class="contact-list">
      <li><svg class="icon"><use href="#icon-phone"/></svg>0400 318 572</li>
      <li><svg class="icon"><use href="#icon-mail"/></svg>daniel@voltaraelectro.com</li>
      <li><svg class="icon"><use href="#icon-globe"/></svg>www.voltaraelectro.com.au</li>
    </ul>
    <div class="side-panel" role="img" aria-label="Silver and electric blue brand decoration area"></div>
  </section>

  <section class="card card-back">
    <div class="brand-name">
      <span class="brand-dot"></span>
      <span><span class="brand-main">VOLTARA</span><span class="brand-sub">ELECTRO SERVICES</span></span>
    </div>
    <p class="tagline">YOUR <strong>TRUSTED</strong> ELECTRICAL CONTRACTOR</p>
    <ul class="services services-left">
      <li>LED Lighting</li>
      <li>Installations</li>
      <li>Maintenance</li>
    </ul>
    <ul class="services services-right">
      <li>Repairs</li>
      <li>Communications</li>
      <li>Emergency Call-Outs</li>
    </ul>
    <div class="quote-band">
      <p>Get in today for your FREE Quotation!</p>
      <p class="quote-contacts">
        <span><svg class="icon"><use href="#icon-phone"/></svg>0400 318572</span>
        <span><svg class="icon"><use href="#icon-mail"/></svg>daniel@voltaraelectro.com</span>
      </p>
    </div>
  </section>
</div>
</body>
</html>
```